Flyer-Design für Empowerment-Coaching
Zielgruppe
Ich bin Empowerment-Coach für FLINK-Lerner, das sind Frauen (zwischen 30-55, angestellt in vorrangig Assistenzfunktionen), die zu nett sind, um nein zu sagen und sich freundlich und selbstbestimmt im Business zu behaupten. Meine Leistungen biete ich vorrangig im Online-Coaching (1:1, Mastermind), aber auch Workshops.
Aufgabenstellung
Farben sollten Webseite und zum Logo passen:
#7AB51D, CMYK: 60/0/100/0
Grau: #707173, CMYK: 0/0/0/70, siehe auch www.begleitung-fuer-flinklerner.de

```html
<!DOCTYPE html>
<html lang="de">
<head>
<meta charset="utf-8">
<title>Flyer – Begleitung für Flinklerner</title>
<link rel="stylesheet" href="https://fonts.googleapis.com/css2?family=Exo+2:wght@300;400;600;700&display=swap">
<style>
  :root {
    --green: #7ab51d;
    --grey: #58595b;
    --text-grey: #4a4a4c;
    --white: #ffffff;
    --sheep-light: #e6dccb;
    --sheep-mid: #c9b99e;
  }
  * { margin: 0; padding: 0; box-sizing: border-box; }
  html, body { width: 1200px; height: 848px; overflow: hidden; background: var(--white); }
  .flyer {
    position: relative; width: 1200px; height: 848px;
    font-family: "Exo 2", sans-serif; color: var(--text-grey);
    background: var(--white); border: 1px solid #cfcfcf;
  }
  .brand-dot {
    position: absolute; left: 792px; top: 72px; width: 70px; height: 70px;
    border-radius: 50%; background: var(--green);
  }
  .brand { position: absolute; right: 68px; top: 52px; text-align: right; }
  .brand-name { font-size: 40px; line-height: 44px; font-weight: 600; color: var(--text-grey); }
  .brand-tagline { margin-top: 10px; font-size: 20px; font-weight: 600; color: var(--text-grey); }
  .question {
    position: absolute; left: 99px; top: 196px;
    font-size: 25px; font-weight: 700; color: var(--green);
  }
  .checklist { position: absolute; left: 100px; top: 230px; list-style: none; }
  .checklist li {
    display: flex; align-items: center; gap: 7px;
    font-size: 19.8px; font-weight: 400; height: 31.5px; color: var(--text-grey);
  }
  .checklist svg { width: 22px; height: 20px; flex: none; }
  .slogan {
    position: absolute; left: 0; width: 1180px; top: 385px; text-align: center;
    font-size: 36px; font-weight: 300; color: var(--green); letter-spacing: 0.5px;
  }
  .slogan strong { font-weight: 700; }
  .program {
    position: absolute; left: 120px; top: 445px; width: 942px; height: 147px;
    background: var(--green); color: var(--white); text-align: center;
  }
  .program-title { margin-top: 14px; font-size: 51px; line-height: 60px; font-weight: 700; padding-right: 10px; }
  .program-sub { margin-top: 0; font-size: 30px; line-height: 40px; font-weight: 400; padding-right: 136px; }
  .mascot {
    position: absolute; left: 848px; top: 522px; width: 302px; height: 202px;
    border-radius: 48% 48% 0 0 / 40% 40% 0 0;
    background: radial-gradient(ellipse at 55% 45%, var(--sheep-light), var(--sheep-mid));
  }
  .cta {
    position: absolute; left: 0; width: 1133px; top: 616px; text-align: center;
    font-size: 21px; font-weight: 400; color: var(--green);
  }
  .cta-phone {
    position: absolute; left: 0; width: 1130px; top: 651px; text-align: center;
    font-size: 35px; font-weight: 700; color: var(--green);
  }
  .footer {
    position: absolute; left: 0; bottom: 0; width: 100%; height: 124px;
    background: var(--grey); color: var(--white); font-size: 17px; line-height: 21.5px;
  }
  .footer-col { position: absolute; top: 15px; }
  .footer-col.contact-person { left: 64px; }
  .footer-col.contact-phone { left: 355px; top: 36px; }
  .footer-col.contact-web { left: 627px; top: 36px; }
  .footer-name { font-weight: 700; }
</style>
</head>
<body>
<div class="flyer">
  <span class="brand-dot"></span>
  <div class="brand">
    <div class="brand-name">Begleitung für<br>Flinklerner</div>
    <div class="brand-tagline">Klar und freundlich im Beruf</div>
  </div>

  <h2 class="question">Sind Sie zu nett für diese Arbeitswelt?</h2>
  <ul class="checklist">
    <li><svg viewBox="0 0 22 20"><path d="M2 11 L8 17 L20 3" fill="none" stroke="#7ab51d" stroke-width="4" stroke-linecap="round" stroke-linejoin="round"/></svg>Bei Ihnen laufen alle Fäden zusammen, aber andere, Ihr Chef, Ihre Kollegen oder Kunden haben Sie in der Hand?</li>
    <li><svg viewBox="0 0 22 20"><path d="M2 11 L8 17 L20 3" fill="none" stroke="#7ab51d" stroke-width="4" stroke-linecap="round" stroke-linejoin="round"/></svg>Sie sind hilfsbereit, fleißig und gewissenhaft, doch erhalten keine Wertschätzung und Anerkennung?</li>
    <li><svg viewBox="0 0 22 20"><path d="M2 11 L8 17 L20 3" fill="none" stroke="#7ab51d" stroke-width="4" stroke-linecap="round" stroke-linejoin="round"/></svg>Sie fühlen Sich oft ausgenutzt?</li>
    <li><svg viewBox="0 0 22 20"><path d="M2 11 L8 17 L20 3" fill="none" stroke="#7ab51d" stroke-width="4" stroke-linecap="round" stroke-linejoin="round"/></svg>Grenzen setzen und Nein sagen fällt Ihnen schwer?</li>
  </ul>

  <p class="slogan">SCHLUSS MIT <strong>LEISE</strong> SEIN!</p>

  <section class="program">
    <h1 class="program-title">Das K.L.A.R.E. - Coaching-Programm</h1>
    <p class="program-sub">In 5 Schritten zu mehr Selbstbestimmung</p>
  </section>

  <div class="mascot" role="img" aria-label="Foto eines zähnefletschenden Schafs"></div>

  <p class="cta">Jetzt kostenloses Beratungsgespräch vereinbaren</p>
  <p class="cta-phone">+49 1570 001 2345</p>

  <footer class="footer">
    <div class="footer-col contact-person">
      <div class="footer-name">Dr. Helene Stavrin</div>
      <div>Coaching | Training Consulting</div>
      <div>Lindenweg 14</div>
      <div>35099 Talbrunn</div>
    </div>
    <div class="footer-col contact-phone">
      <div>Telefon: +49 6400 123456</div>
      <div>Mobil: +49 1570 0012345</div>
      <div>Fax: 06400 123457</div>
    </div>
    <div class="footer-col contact-web">
      <div>stavrin@begleitung-fuer-flinklerner.de</div>
      <div>www.begleitung-fuer-flinklerner.de</div>
    </div>
  </footer>
</div>
</body>
</html>
```